New veltrix brand project - Label improvements

We are creating a brand for a large online retailer and are in need of some retouching on some ideas we have. I have already had a go at a design and four labels concepts we think are going to work. On the labels I have created it is important that the look of the label stays the same over the four designs but show how the flavour differ.<br/>The design need to show past link to trading routes possibly using some form of map in the background of the label.<br/><br/>What we need from you is to;<br/>- Provide finishing touches and illustrations for labels.<br/>- Show a transparent part of the label to reveal image on the reverse side. <br/>- Show a connection to trade routes throughout the globe.

Colors

Designer to choose colors to be used in the design.

Requirements
Must have
• - Transparency on label to view image on reverse.
• - Nautical theme.
• - Ropes on label
• - Brand colours of Dark blue and gold on logo
• - Brand Font on label
• - Legal info.
Nice to have
• - Map in background
• - Wavy trim.
Should not have
• - Any mention of veltrix.

```html
<!DOCTYPE html>
<html lang="en">
<head>
<meta charset="utf-8">
<title>Marivane Spirits – Valencian Orange Gin Label</title>
<link href="https://fonts.googleapis.com/css2?family=Josefin+Sans:wght@300;400;600&family=Montserrat:wght@600;700&display=swap" rel="stylesheet">
<style>
  :root {
    --page: #ffffff;
    --label-white: #f7f6f4;
    --panel-cream: #efe3d0;
    --frame-ink: #2b2a30;
    --navy: #2c2c5a;
    --ink: #2a2a2a;
    --muted-ink: #5a5a5e;
    --art-green: #9fb59a;
    --art-sand: #e4d6bd;
  }
  * { box-sizing: border-box; margin: 0; padding: 0; }
  html, body { width: 900px; height: 1200px; overflow: hidden; background: var(--page); }
  .canvas {
    width: 900px; height: 1200px; position: relative;
    display: flex; align-items: center; justify-content: center;
  }
  .label {
    width: 600px; height: 860px; background: var(--label-white);
    position: relative; box-shadow: 0 0 0 1px #e6e3df;
  }
  .panel {
    position: absolute; left: 50px; right: 50px; top: 40px; bottom: 40px;
    background: var(--panel-cream);
  }
  .panel-frame {
    position: absolute; left: 22px; right: 22px; top: 30px; bottom: 22px;
    border: 2px solid var(--frame-ink);
  }
  .brand-band {
    position: absolute; left: 0; right: 0; top: 110px; height: 130px;
    background: var(--label-white);
    display: flex; flex-direction: column; align-items: center; justify-content: center;
  }
  .brand-name {
    font-family: "Montserrat", sans-serif; font-weight: 700;
    font-size: 64px; letter-spacing: 3px; color: var(--navy); line-height: 1;
  }
  .brand-sub {
    font-family: "Josefin Sans", sans-serif; font-weight: 400;
    font-size: 36px; letter-spacing: 12px; color: var(--ink);
    margin-top: 8px; padding-left: 12px; line-height: 1;
  }
  .illustration {
    position: absolute; left: 90px; right: 90px; top: 262px; height: 270px;
    background: radial-gradient(ellipse at 50% 50%, var(--art-green) 0%, var(--art-sand) 100%);
  }
  .flavour-band {
    position: absolute; left: 0; right: 0; top: 545px; height: 64px;
    background: var(--label-white);
    display: flex; align-items: center; justify-content: center;
    font-family: "Montserrat", sans-serif; font-weight: 600;
    font-size: 28px; letter-spacing: 1px; color: var(--muted-ink);
  }
  .detail {
    position: absolute; font-family: "Josefin Sans", sans-serif; color: var(--ink); line-height: 1;
  }
  .volume { left: 70px; top: 642px; font-size: 22px; font-weight: 300; }
  .abv { right: 70px; top: 634px; font-size: 22px; font-weight: 300; }
  .origin {
    left: 180px; right: 0; top: 706px; text-align: center;
    font-family: "Montserrat", sans-serif; font-weight: 700; font-size: 11px; letter-spacing: 0.5px;
  }
  .batch { left: 70px; top: 740px; font-size: 24px; font-weight: 300; letter-spacing: 4px; }
</style>
</head>
<body>
  <main class="canvas">
    <section class="label">
      <div class="panel">
        <div class="panel-frame"></div>
        <div class="brand-band">
          <div class="brand-name">MARIVANE</div>
          <div class="brand-sub">SPIRITS</div>
        </div>
        <div class="illustration" role="img" aria-label="Illustration area: orange tree with a twisted rope trunk, green leaves and orange fruit"></div>
        <div class="flavour-band">VALENCIAN ORANGE GIN</div>
        <div class="detail volume">70cl</div>
        <div class="detail abv">40%vol</div>
        <div class="detail origin">MADE IN MERSEYSIDE</div>
        <div class="detail batch">BATCH :</div>
      </div>
    </section>
  </main>
</body>
</html>
```